Etiketten-Design für Roséwein & Weißwein
Zielgruppe
Wir sind eine Weinkellerei, die einfache Trinkweine für den LEH herstellt.
Unsere Zielgruppen sind Personen ab 16 Jahren.
Aufgabenstellung
Das Etikett sollte ein Pulvereffekt mit Wasserfarbe sein.
Sorten Roséwein und Weißwein
Gerne können Sie auch Ihren kreativen Gedanken freien Lauf lassen und etwas eigenes designen.

```html
<!DOCTYPE html>
<html lang="de">
<head>
<meta charset="utf-8">
<title>Etiketten – Weißwein &amp; Rosé</title>
<link rel="stylesheet" href="https://fonts.googleapis.com/css2?family=Great+Vibes&display=swap">
<style>
  :root {
    --canvas: #ffffff;
    --paper: #fbfbf9;
    --label-text: #ffffff;
    --white-wine-deep: #6fbf3a;
    --white-wine-mid: #9fd46a;
    --white-wine-light: #d8eec4;
    --white-wine-accent: #e9d44a;
    --rose-deep: #c52f8e;
    --rose-mid: #d962a8;
    --rose-light: #ecc3dc;
    --rose-accent: #8a4aa6;
  }
  * { margin: 0; padding: 0; box-sizing: border-box; }
  html, body {
    width: 1200px;
    height: 1200px;
    overflow: hidden;
    background: var(--canvas);
  }
  .label-sheet {
    position: relative;
    width: 1200px;
    height: 1200px;
    display: flex;
    justify-content: center;
    align-items: center;
    gap: 90px;
  }
  .wine-label {
    position: relative;
    width: 470px;
    height: 716px;
    border-radius: 22px;
    overflow: hidden;
    background: var(--paper);
  }
  .watercolour {
    position: absolute;
    inset: 0;
  }
  .wine-label--white .watercolour {
    background:
      radial-gradient(ellipse 55% 60% at 58% 62%,
        var(--white-wine-deep) 0%,
        var(--white-wine-mid) 40%,
        var(--white-wine-light) 72%,
        rgba(251,251,249,0) 100%);
  }
  .wine-label--rose .watercolour {
    background:
      radial-gradient(ellipse 62% 58% at 55% 58%,
        var(--rose-deep) 0%,
        var(--rose-mid) 45%,
        var(--rose-light) 75%,
        rgba(251,251,249,0) 100%);
  }
  .wine-label__name {
    position: absolute;
    left: 0;
    right: 0;
    top: 45%;
    text-align: center;
    font-family: "Great Vibes", cursive;
    font-weight: 400;
    color: var(--label-text);
    line-height: 1;
  }
  .wine-label--white .wine-label__name {
    font-size: 112px;
    padding-left: 24px;
  }
  .wine-label--rose .wine-label__name {
    font-size: 128px;
    top: 43%;
  }
</style>
</head>
<body>
  <main class="label-sheet">
    <section class="wine-label wine-label--white">
      <div class="watercolour" role="img" aria-label="Aquarell-Pulverexplosion in Grün mit gelben Akzenten"></div>
      <h2 class="wine-label__name">Weißwein</h2>
    </section>
    <section class="wine-label wine-label--rose">
      <div class="watercolour" role="img" aria-label="Aquarell-Pulverexplosion in Magenta und Violett"></div>
      <h2 class="wine-label__name">Rosè</h2>
    </section>
  </main>
</body>
</html>
```